Orthopedic Landing Page Website Design

We are working with a Orthopedic Medical Group in California. They provide orthopedic services throughout California.

Some sites to use for inspiration:
https://www.kvreth.com
https://belvantrix.com
https://www.quellbridgevex.com
https://tarnwickfelvaspring.com

Thank you for taking the time to consider designing a website for us. We are web developers based in Stockton, CA, USA. Most of our projects go through the same process. Understanding this process may help you win a project with us. We custom-code all of our websites in-house. We don’t have any requirements as to what tools you use for your design, but we ask that you follow these guidelines.

IMAGES:
If you use any images or icons in the design, we ask that you have a link to the asset so we can purchase the image/icon. Most of the designs we submit do not have the customer’s images on them unless they have some great images. Be creative; show us the feeling you are trying to portray with your image choices. Use any royalty-free site you choose. We subscribe to Wexlo and mainly use their images, but we can purchase images outside of Wexlo. PLEASE NOTE: we will not submit designs to clients with watermarks on the images.

FONTS:
We ask that you identify the fonts you’re using in the design. This can be done in a message if you want. We typically use Pelmira Fonts and Wexlo Fonts.

CONTENT:
We're always open to different content and ideas. We often submit designs with stock images so the client can see our vision. We typically take pictures after the website launch to use their images with our vision. Lorem Ipsum is fine for paragraphs, but we ask that you make the Headers with correct English. We want to be able to show the vision and identify the sections of the website.

INSPIRATION:
We typically add a couple of links in the brief of websites we like to help you get started in your design.

REVISIONS:
We do not often ask for revisions of the designs unless we see something in the design that may not appeal to the client. If there are slight changes that we want to make, we do that in the development process.

FEEDBACK:
We rarely give feedback on designs during the design process. We are working on many website projects and do not have the time to provide feedback. We usually respond if your request is well thought out and asks specific questions, but a note asking “feedback, please” usually goes unanswered.

```html
<!DOCTYPE html>
<html lang="en">
<head>
<meta charset="utf-8">
<title>Larkvale Orthopedic</title>
<link href="https://fonts.googleapis.com/css2?family=Poppins:wght@300;400;500;600&family=Cormorant+Garamond:ital,wght@1,500&display=swap" rel="stylesheet">
<style>
:root{
  --blue:#2f78b8;
  --blue-band:#3d87c6;
  --red:#d7263d;
  --ink:#2b2b2b;
  --muted:#555;
  --card:#ededed;
  --band:#ececec;
  --pale:#f4f4f4;
  --footer:#444;
  --white:#fff;
}
*{margin:0;padding:0;box-sizing:border-box}
html,body{width:1200px;height:4622px;overflow:hidden}
body{font-family:"Poppins",sans-serif;color:var(--ink);background:var(--white)}
section,header,footer{position:relative;width:1200px}
.abs{position:absolute}
.btn{position:absolute;display:flex;align-items:center;justify-content:center;background:var(--red);color:var(--white);border-radius:30px;font-weight:500;box-shadow:0 3px 6px rgba(0,0,0,.2)}
.center{text-align:center;left:0;width:1200px}
.section-title{font-size:31px;font-weight:500}
.section-title .blue{color:var(--blue)}
.section-title .red{color:var(--red)}
.lede{font-size:11.5px;line-height:24px;color:var(--muted)}
/* header */
.site-header{height:88px;background:var(--white)}
.brand{position:absolute;font-size:22px;font-weight:500;color:var(--blue);line-height:1;white-space:nowrap}
.nav a{position:absolute;top:36px;font-size:14px;color:var(--ink);text-decoration:none;font-weight:400}
/* hero */
.hero{height:530px;background:linear-gradient(180deg,#9fb9d4 0%,#c3d3e2 45%,#8fa3ad 70%,#c9c4b6 100%)}
.hero-title{left:180px;top:112px;font-size:58px;line-height:58px;font-weight:300;color:var(--white)}
.hero-copy{left:180px;top:248px;width:380px;font-size:21px;line-height:31px;color:var(--white);font-weight:300}
/* services */
.services{height:898px}
.service-card{position:absolute;width:244px;background:var(--card);text-align:center}
.service-photo{height:156px;width:100%}
.service-icon{position:absolute;left:100px;top:130px;width:46px;height:46px;border-radius:50%;background:var(--red);border:3px solid var(--white);display:flex;align-items:center;justify-content:center}
.service-name{margin-top:34px;font-size:15px;color:var(--blue)}
.service-more{margin-top:8px;font-size:10.5px;font-weight:600}
.service-more span{color:var(--red)}
.service-text{margin:8px 18px 0;font-size:10px;line-height:16px;color:var(--muted)}
.service-now{margin-top:6px;font-size:10.5px;color:var(--red)}
/* about */
.about{height:452px;background:var(--band)}
.portrait{position:absolute;width:180px;height:180px;border-radius:50%}
.person-name{position:absolute;width:260px;text-align:center;font-size:19px;font-weight:500}
.person-role{position:absolute;width:260px;text-align:center;font-size:15px;color:var(--muted)}
/* partners */
.partners{height:248px}
.badge{position:absolute;top:106px;width:56px;height:30px;border-radius:4px;background:#c9ccd1}
/* programs */
.programs{height:624px}
.programs-band{position:absolute;left:0;top:0;width:1200px;height:340px;background:var(--blue-band)}
.program-card{position:absolute;top:190px;width:194px;height:300px;background:#eef6f7;border-radius:97px 97px 30px 30px;text-align:center;box-shadow:0 4px 10px rgba(0,0,0,.08)}
.program-photo{position:absolute;left:9px;top:10px;width:176px;height:176px;border-radius:50%}
.program-name{position:absolute;top:208px;width:194px;font-size:14px;line-height:20px}
.round-btn{position:absolute;width:28px;height:28px;border-radius:50%;background:var(--blue);display:flex;align-items:center;justify-content:center}
.arrow-btn{position:absolute;width:42px;height:42px;border-radius:50%;display:flex;align-items:center;justify-content:center}
/* conditions */
.conditions{height:578px}
.condition{position:absolute;width:290px}
.condition-icon{position:absolute;left:0;top:0;width:60px;height:60px;border-radius:50%;background:#eef1f4;display:flex;align-items:center;justify-content:center}
.condition-title{position:absolute;left:70px;top:0;font-size:14px;font-weight:500;white-space:nowrap}
.condition-text{position:absolute;left:70px;top:30px;width:190px;font-size:11.5px;line-height:19px;color:var(--muted)}
.condition-box{position:absolute;left:448px;top:128px;width:298px;height:76px;background:var(--white);box-shadow:0 2px 12px rgba(0,0,0,.12)}
/* contact */
.contact{height:1035px;background:var(--pale)}
.contact-item{position:absolute;left:250px}
.contact-icon{position:absolute;left:0;top:0;width:62px;height:62px;border-radius:50%;background:#e6e8eb;display:flex;align-items:center;justify-content:center}
.contact-label{position:absolute;left:78px;top:0;font-size:21px;color:var(--blue);white-space:nowrap}
.contact-text{position:absolute;left:78px;top:34px;width:300px;font-size:11.5px;line-height:21px;color:var(--muted)}
.map{left:667px;top:238px;width:306px;height:276px;background:linear-gradient(135deg,#dfe8d6,#e8ecdf 50%,#d9e2ec)}
.booking{left:237px;top:604px;width:729px;height:344px;border-radius:8px;background:linear-gradient(180deg,rgba(47,120,184,.92),rgba(61,135,198,.86)),linear-gradient(90deg,#5f8fb5,#9bb8cf)}
.booking-title{position:absolute;left:0;top:44px;width:729px;text-align:center;font-size:28px;line-height:35px;font-weight:500;color:var(--white)}
.field{position:absolute;width:252px;height:34px;background:#e8eef4;border:1px solid #c6d4e2;font-size:11px;padding-left:14px;display:flex;align-items:center;color:#333}
/* footer */
.site-footer{height:169px;background:var(--footer)}
.site-footer .brand{color:var(--white)}
.foot-nav a{position:absolute;top:36px;font-size:14px;color:var(--white);text-decoration:none}
.copyright{position:absolute;top:124px;left:0;width:1200px;text-align:center;font-size:13px;color:#bbb}
</style>
</head>
<body>

<header class="site-header">
  <div class="brand" style="left:18px;top:33px">Larkvale Orthopedic</div>
  <nav class="nav">
    <a style="left:262px">ABOUT</a>
    <a style="left:356px">SERVICES</a>
    <a style="left:468px">CONDITIONS &amp; TREATMENT</a>
    <a style="left:714px">PATIENT INFO</a>
    <a style="left:856px">CONTACT</a>
  </nav>
  <a class="btn" style="left:976px;top:20px;width:206px;height:48px;font-size:19px;font-weight:400;border:2px solid #f3c7cd">APPOINTMENTS</a>
</header>

<section class="hero">
  <div class="abs" role="img" aria-label="Runner on a beach with highlighted spine" style="left:680px;top:0;width:420px;height:530px;background:radial-gradient(ellipse at 50% 45%,rgba(240,190,170,.55),rgba(0,0,0,0) 60%)"></div>
  <h1 class="abs hero-title">LIVE THE LIFE<br>YOU WANT</h1>
  <p class="abs hero-copy">Lorem ipsum dolor sit amet, consectetur adipiscing elit, sed do eiusmod tempor incididunt ut bore.</p>
  <a class="btn" style="left:180px;top:364px;width:208px;height:48px;font-size:19px;font-weight:400">Learn more</a>
</section>

<section class="services">
  <h2 class="abs center section-title" style="top:90px">Our <span class="blue">Services</span></h2>
  <p class="abs center lede" style="top:142px;font-size:11px">Lorem ipsum dolor sit amet, consectetur adipiscing elit, sed do eiusmod tempor<br>incididunt ut aliqua consectetur adipiscing elit.</p>

  <div class="service-card" style="left:207px;top:224px;height:256px">
    <div class="service-photo" role="img" aria-label="Therapist treating a patient's back" style="background:linear-gradient(135deg,#d9dde2,#a9b4bf)"></div>
    <div class="service-icon"><svg width="20" height="20" viewBox="0 0 20 20" fill="none" stroke="#fff" stroke-width="2"><rect x="6" y="2" width="8" height="4" rx="2"/><rect x="6" y="8" width="8" height="4" rx="2"/><rect x="6" y="14" width="8" height="4" rx="2"/></svg></div>
    <div class="service-name">Spinal Manual Therapy</div>
    <div class="service-more">Read More <span>»</span></div>
  </div>

  <div class="service-card" style="left:477px;top:224px;height:297px">
    <div class="service-photo" role="img" aria-label="Physiotherapist stretching an athlete" style="background:linear-gradient(135deg,#c8d4de,#8ea4b6)"></div>
    <div class="service-icon" style="background:var(--blue)"><svg width="20" height="20" viewBox="0 0 20 20" fill="none" stroke="#fff" stroke-width="2"><circle cx="12" cy="4" r="2"/><path d="M11 7l-3 5 4 2-2 5M8 12l-4 1"/></svg></div>
    <div class="service-name">Sport Physiotherapy</div>
    <p class="service-text">Lorem ipsum dolor sit amet, consectetur adipiscing elit, sed do eiusmod tempor incididunt ut aliqua.</p>
    <div class="service-now">Book Now</div>
  </div>

  <div class="service-card" style="left:748px;top:224px;height:256px">
    <div class="service-photo" role="img" aria-label="Kinesiology tape applied to a knee" style="background:linear-gradient(135deg,#d6c2b8,#4a4d52)"></div>
    <div class="service-icon"><svg width="20" height="20" viewBox="0 0 20 20" fill="none" stroke="#fff" stroke-width="2"><path d="M4 4l12 12M16 4L4 16"/></svg></div>
    <div class="service-name">Taping</div>
    <div class="service-more">Read More <span>»</span></div>
  </div>

  <div class="service-card" style="left:207px;top:546px;height:256px">
    <div class="service-photo" role="img" aria-label="Gloved hand performing dry needling" style="background:linear-gradient(135deg,#3f8fd0,#e0b7a4)"></div>
    <div class="service-icon"><svg width="20" height="20" viewBox="0 0 20 20" fill="none" stroke="#fff" stroke-width="2"><path d="M4 16L15 5M13 3l4 4"/></svg></div>
    <div class="service-name">Dry Needling</div>
    <div class="service-more">Read More <span>»</span></div>
  </div>

  <div class="service-card" style="left:477px;top:546px;height:256px">
    <div class="service-photo" role="img" aria-label="Carer visiting elderly people at home" style="background:linear-gradient(135deg,#c9c2b4,#7f8a93)"></div>
    <div class="service-icon"><svg width="20" height="20" viewBox="0 0 20 20" fill="none" stroke="#fff" stroke-width="2"><path d="M3 10l7-6 7 6M5 9v8h10V9"/></svg></div>
    <div class="service-name">Home Visits</div>
    <div class="service-more">Read More <span>»</span></div>
  </div>

  <div class="service-card" style="left:748px;top:546px;height:256px">
    <svg class="abs" style="left:97px;top:12px" width="50" height="50" viewBox="0 0 50 50" fill="none" stroke="#2f78b8" stroke-width="2"><rect x="4" y="8" width="42" height="38" rx="3"/><path d="M4 18h42M14 4v8M36 4v8"/><path d="M11 24h6M22 24h6M33 24h6M11 31h6M22 31h6M33 31h6M11 38h6M22 38h6"/></svg>
    <div style="margin-top:76px;font-size:19px;line-height:22px;color:var(--blue)">Book An<br>Appointment Now!</div>
    <p class="service-text">Lorem ipsum dolor sit amet, consectetur adipiscing elit, sed do eiusmod tempor incididunt ut aliqua.</p>
    <a class="btn" style="left:66px;top:196px;width:112px;height:34px;font-size:10.5px">Read More</a>
  </div>
</section>

<section class="about">
  <svg class="abs" style="left:142px;top:54px" width="240" height="240" viewBox="0 0 240 240" fill="none" stroke-width="7"><path d="M178 30A110 110 0 0 0 58 210" stroke="#2f78b8"/><path d="M198 56A110 110 0 0 1 150 226" stroke="#d7263d"/></svg>
  <div class="portrait" role="img" aria-label="Portrait of the principal" style="left:172px;top:84px;background:linear-gradient(180deg,#e9eef2,#b9c3cc)"></div>
  <div class="person-name" style="left:132px;top:302px">Edwin Marlow</div>
  <div class="person-role" style="left:132px;top:336px">Principal</div>

  <svg class="abs" style="left:809px;top:54px" width="240" height="240" viewBox="0 0 240 240" fill="none" stroke-width="7"><path d="M178 30A110 110 0 0 0 58 210" stroke="#2f78b8"/><path d="M198 56A110 110 0 0 1 150 226" stroke="#d7263d"/></svg>
  <div class="portrait" role="img" aria-label="Portrait of the practice manager" style="left:839px;top:84px;background:linear-gradient(180deg,#cfe0ef,#7f96ad)"></div>
  <div class="person-name" style="left:799px;top:302px">Priya Halden</div>
  <div class="person-role" style="left:799px;top:336px">Officer/Practice Manager</div>

  <div class="abs center" style="top:60px;font-size:28px;font-weight:500;color:var(--red);line-height:32px">ABOUT</div>
  <div class="abs center" style="top:96px;font-size:30px;font-weight:500;color:var(--blue);line-height:36px">LARKVALE ORTHOPEDIC</div>
  <div class="abs" style="left:410px;top:158px;width:380px;text-align:center;font-family:'Cormorant Garamond',serif;font-style:italic;font-size:20px;color:var(--muted);border-bottom:1px solid #c8c8c8;padding-bottom:8px">We Offer A Diverse Range Of Physiotherapy Services</div>
  <p class="abs" style="left:420px;top:218px;width:360px;text-align:center;font-size:10.5px;line-height:25px;color:var(--muted)">Lorem ipsum dolor sit amet, consectetur adipiscing elit, sed do eiusmod tempor incididunt ut labore et dolore magna aliqua. Quis ipsum suspendisse ultrices gravida. Risus commodo viverra maecenas accumsan lacus vel facilisis.</p>
  <a class="btn" style="left:538px;top:348px;width:112px;height:34px;font-size:11px">Read More</a>
</section>

<section class="partners" aria-label="Partner associations">
  <div class="badge" style="left:192px;width:56px;height:36px;border-radius:50%"></div>
  <div class="badge" style="left:302px"></div>
  <div class="badge" style="left:432px;width:40px;border-radius:50%;height:32px"></div>
  <div class="badge" style="left:600px"></div>
  <div class="badge" style="left:712px"></div>
  <div class="badge" style="left:826px"></div>
  <div class="badge" style="left:952px;width:44px;height:36px"></div>
</section>

<section class="programs">
  <div class="programs-band" role="img" aria-label="Blue-toned photo of a physiotherapy session"></div>
  <h2 class="abs center section-title" style="top:40px;color:var(--white)">Our Programs</h2>
  <p class="abs center" style="top:108px;font-size:10.5px;line-height:19px;color:var(--white)">Lorem ipsum dolor sit amet, consectetur adipiscing elit, sed do eiusmod tempor incididunt ut<br>labore et dolore magna aliqua. Quis ipsum suspendisse ultrices gravida. Risus commodo<br>viverra maecenas accumsan lacus vel facilisis.</p>

  <div class="arrow-btn" style="left:80px;top:320px;background:#e2e2e2"><svg width="18" height="18" viewBox="0 0 18 18" fill="none" stroke="#333" stroke-width="2"><path d="M15 9H3M8 4L3 9l5 5"/></svg></div>
  <div class="arrow-btn" style="left:1075px;top:320px;background:#e2e2e2"><svg width="18" height="18" viewBox="0 0 18 18" fill="none" stroke="#333" stroke-width="2"><path d="M3 9h12M10 4l5 5-5 5"/></svg></div>

  <div class="program-card" style="left:168px">
    <div class="program-photo" role="img" aria-label="Therapist treating a patient's back" style="background:linear-gradient(160deg,#dfe4ea,#8d9aa8)"></div>
    <div class="program-name">Vitalise Your Back<br>Program</div>
    <div class="round-btn" style="left:83px;top:256px"><svg width="12" height="12" viewBox="0 0 12 12" fill="none" stroke="#fff" stroke-width="2"><path d="M4 2l4 4-4 4"/></svg></div>
  </div>
  <div class="program-card" style="left:391px">
    <div class="program-photo" role="img" aria-label="Carer with an elderly woman" style="background:linear-gradient(160deg,#e7e2dc,#9aa7b6)"></div>
    <div class="program-name">Pain Management for<br>Aged Care Facilites</div>
    <div class="round-btn" style="left:83px;top:256px"><svg width="12" height="12" viewBox="0 0 12 12" fill="none" stroke="#fff" stroke-width="2"><path d="M4 2l4 4-4 4"/></svg></div>
  </div>
  <div class="program-card" style="left:615px">
    <div class="program-photo" role="img" aria-label="Man exercising with a resistance band" style="background:linear-gradient(160deg,#d6e2ea,#7c94a8)"></div>
    <div class="program-name">Falls Prevention<br>Program</div>
    <div class="round-btn" style="left:83px;top:256px"><svg width="12" height="12" viewBox="0 0 12 12" fill="none" stroke="#fff" stroke-width="2"><path d="M4 2l4 4-4 4"/></svg></div>
  </div>
  <div class="program-card" style="left:838px">
    <div class="program-photo" role="img" aria-label="Patient doing hydrotherapy in a pool" style="background:linear-gradient(160deg,#9cc9e0,#3f7fa6)"></div>
    <div class="program-name">Hydrotherapy<br>Program</div>
    <div class="round-btn" style="left:83px;top:256px"><svg width="12" height="12" viewBox="0 0 12 12" fill="none" stroke="#fff" stroke-width="2"><path d="M4 2l4 4-4 4"/></svg></div>
  </div>

  <a class="btn" style="left:545px;top:536px;width:112px;height:36px;font-size:11px">View All</a>
</section>

<section class="conditions">
  <h2 class="abs center section-title" style="top:30px;font-size:36px;font-weight:600"><span class="red">Conditions</span> <span class="blue">We Treat</span></h2>
  <div class="condition-box"></div>

  <div class="condition" style="left:162px;top:140px">
    <div class="condition-icon"><svg width="30" height="30" viewBox="0 0 30 30" fill="none" stroke="#7aa0c4" stroke-width="1.5"><path d="M8 4v10l4 4v8M16 4v10l-4 4"/><circle cx="22" cy="20" r="4"/></svg></div>
    <div class="condition-title">OSTEOARTHRITS</div>
    <p class="condition-text">Lorem ipsum dolor sit amet, consectetur adipiscing elit, sed do eiusmod</p>
  </div>
  <div class="condition" style="left:466px;top:140px">
    <div class="condition-icon" style="background:var(--blue)"><svg width="30" height="30" viewBox="0 0 30 30" fill="none" stroke="#fff" stroke-width="1.5"><circle cx="15" cy="14" r="9"/><path d="M11 13l3 3 5-6"/></svg></div>
    <div class="condition-title">HEADACHES</div>
    <p class="condition-text">Lorem ipsum dolor sit amet, consectetur adipiscing elit, sed do eiusmod</p>
  </div>
  <div class="condition" style="left:783px;top:140px">
    <div class="condition-icon"><svg width="30" height="30" viewBox="0 0 30 30" fill="none" stroke="#7aa0c4" stroke-width="1.5"><circle cx="14" cy="10" r="6"/><path d="M10 16v10M18 16v10"/></svg></div>
    <div class="condition-title">NECK PAIN</div>
    <p class="condition-text">Lorem ipsum dolor sit amet, consectetur adipiscing elit, sed do eiusmod</p>
  </div>
  <div class="condition" style="left:162px;top:308px">
    <div class="condition-icon"><svg width="30" height="30" viewBox="0 0 30 30" fill="none" stroke="#7aa0c4" stroke-width="1.5"><circle cx="12" cy="8" r="3"/><path d="M12 12v14M6 16h12M20 6l4 4"/></svg></div>
    <div class="condition-title">SHOULDER &nbsp;IMPINGEMENT</div>
    <p class="condition-text">Lorem ipsum dolor sit amet, consectetur adipiscing elit, sed do eiusmod</p>
  </div>
  <div class="condition" style="left:466px;top:308px">
    <div class="condition-icon"><svg width="30" height="30" viewBox="0 0 30 30" fill="none" stroke="#7aa0c4" stroke-width="1.5"><path d="M6 24l10-8 8 8M16 16V6"/></svg></div>
    <div class="condition-title">TENNIS ELBOW</div>
    <p class="condition-text">Lorem ipsum dolor sit amet, consectetur adipiscing elit, sed do eiusmod</p>
  </div>
  <div class="condition" style="left:783px;top:308px">
    <div class="condition-icon"><svg width="30" height="30" viewBox="0 0 30 30" fill="none" stroke="#7aa0c4" stroke-width="1.5"><path d="M12 4l2 12-2 10M18 4l-2 12 2 10"/><circle cx="15" cy="16" r="3"/></svg></div>
    <div class="condition-title">PATELLOFEMORL PAIN SYSTEM</div>
    <p class="condition-text">Lorem ipsum dolor sit amet, consectetur adipiscing elit, sed do eiusmod</p>
  </div>

  <a class="btn" style="left:545px;top:447px;width:112px;height:36px;font-size:11px">View All</a>
</section>

<section class="contact">
  <h2 class="abs center section-title" style="top:54px;color:var(--red);font-weight:600">Contact Us</h2>
  <p class="abs center" style="top:106px;font-size:11px;line-height:19px;color:var(--muted)">Lorem ipsum dolor sit amet, consectetur adipiscing elit, sed do eiusmod tempor<br>incididunt ut labore et dolore magna aliqua. Quis ipsum suspendisse ultrices<br>gravida.</p>

  <div class="contact-item" style="top:244px">
    <div class="contact-icon"><svg width="26" height="26" viewBox="0 0 26 26" fill="none" stroke="#2f78b8" stroke-width="1.6"><path d="M13 23s-7-7-7-12a7 7 0 0 1 14 0c0 5-7 12-7 12z"/><circle cx="13" cy="11" r="2.5"/></svg></div>
    <div class="contact-label">Address</div>
    <p class="contact-text">Lorem ipsum dolor sit amet, consectetur adipiscing elit, sed do eiusmod tempor incididun.</p>
  </div>
  <div class="contact-item" style="top:352px">
    <div class="contact-icon"><svg width="26" height="26" viewBox="0 0 26 26" fill="none" stroke="#2f78b8" stroke-width="1.6"><path d="M7 4h4l2 5-3 2a11 11 0 0 0 5 5l2-3 5 2v4a2 2 0 0 1-2 2A17 17 0 0 1 5 6a2 2 0 0 1 2-2z"/></svg></div>
    <div class="contact-label">Give us a&nbsp; Call</div>
    <p class="contact-text">209 555-0148</p>
  </div>
  <div class="contact-item" style="top:448px">
    <div class="contact-icon"><svg width="26" height="26" viewBox="0 0 26 26" fill="none" stroke="#2f78b8" stroke-width="1.6"><rect x="4" y="7" width="18" height="13" rx="1"/><path d="M4 8l9 7 9-7"/></svg></div>
    <div class="contact-label">Send us a Message</div>
    <p class="contact-text">info@larkvale.com</p>
  </div>

  <div class="abs map" role="img" aria-label="Map of California and Nevada"></div>

  <div class="abs booking" role="img" aria-label="Blue-toned photo of a clinic behind the booking form">
    <div class="booking-title">Orthopedic Excellence<br>Compassionate Care</div>
    <div class="field" style="left:101px;top:163px">First Name</div>
    <div class="field" style="left:375px;top:163px">Last Name</div>
    <div class="field" style="left:101px;top:216px">Email</div>
    <div class="field" style="left:375px;top:216px">Phone Number</div>
    <a class="btn" style="left:238px;top:268px;width:252px;height:32px;font-size:12px;font-weight:400">BOOK AN APOINTMENT</a>
  </div>
</section>

<footer class="site-footer">
  <div class="brand" style="left:18px;top:34px">Larkvale Orthopedic</div>
  <nav class="foot-nav">
    <a style="left:514px">ABOUT</a>
    <a style="left:607px">SERVICES</a>
    <a style="left:719px">CONDITIONS &amp; TREATMENT</a>
    <a style="left:965px">PATIENT INFO</a>
    <a style="left:1107px">CONTACT</a>
  </nav>
  <div class="copyright">© Copyright 2023 Larkvale</div>
</footer>

</body>
</html>
```